Visitenkarte erstellen für Reiki Praxis

Visitenkarten für Reiki Praxis Doppelseitig

business cards reiki practice double-sided

The background can also be a different color

```html
<!DOCTYPE html>
<html lang="de">
<head>
<meta charset="utf-8">
<title>Seelenlicht – Visitenkarte</title>
<link href="https://fonts.googleapis.com/css2?family=Montserrat:wght@400;500;600&display=swap" rel="stylesheet">
<style>
  :root {
    --backdrop: #e9e4dc;
    --card-purple: #7b5ba6;
    --gold: #e2a62b;
    --white: #ffffff;
    --shadow: rgba(0, 0, 0, 0.35);
  }
  * { margin: 0; padding: 0; box-sizing: border-box; }
  html, body {
    width: 900px;
    height: 1200px;
    overflow: hidden;
    background: var(--backdrop);
    font-family: "Montserrat", Arial, sans-serif;
  }
  .stage { position: relative; width: 900px; height: 1200px; }

  .card {
    position: absolute;
    left: 80px;
    width: 742px;
    height: 440px;
    border-radius: 40px;
    background: var(--card-purple);
    box-shadow: 0 4px 14px var(--shadow);
  }
  .card--front { top: 132px; }
  .card--back { top: 638px; }

  /* Front: brand block */
  .brand {
    position: absolute;
    text-align: center;
    color: var(--gold);
    font-weight: 400;
  }
  .brand__dot {
    display: block;
    margin: 0 auto;
    border-radius: 50%;
    background: var(--gold);
  }
  .card--front .brand { left: 73px; top: 150px; width: 300px; }
  .card--front .brand__dot { width: 44px; height: 44px; margin-bottom: 28px; }
  .card--front .brand__name { font-size: 32px; line-height: 34px; letter-spacing: 0.5px; }
  .card--front .brand__person { font-size: 21px; line-height: 28px; letter-spacing: 4px; }

  .divider {
    position: absolute;
    left: 412px;
    top: 113px;
    width: 2px;
    height: 218px;
    background: var(--gold);
  }

  .contact { position: absolute; left: 465px; top: 106px; color: var(--white); }
  .contact__name { font-size: 22px; font-weight: 600; color: var(--gold); line-height: 28px; }
  .contact__role { font-size: 15px; line-height: 20px; }
  .contact__list { list-style: none; margin-top: 34px; }
  .contact__item {
    display: flex;
    align-items: center;
    font-size: 15.5px;
    height: 26.5px;
  }
  .contact__icon { width: 14px; height: 14px; margin-right: 16px; fill: var(--gold); }
  .contact__address { margin-top: 27px; font-size: 15.5px; line-height: 20px; }

  /* Back */
  .card--back .brand { left: 0; width: 742px; top: 95px; }
  .card--back .brand__dot { width: 90px; height: 90px; margin-bottom: 70px; }
  .card--back .brand__name { font-size: 52px; line-height: 60px; letter-spacing: 1px; }
  .card--back .brand__person { font-size: 36px; line-height: 46px; letter-spacing: 7px; }
</style>
</head>
<body>
<main class="stage">
  <section class="card card--front" aria-label="Vorderseite">
    <div class="brand">
      <span class="brand__dot"></span>
      <div class="brand__name">SEELENLICHT</div>
      <div class="brand__person">MIRA LENZ</div>
    </div>
    <div class="divider"></div>
    <div class="contact">
      <div class="contact__name">Mira Lenz</div>
      <div class="contact__role">CEO &amp; Founder</div>
      <ul class="contact__list">
        <li class="contact__item">
          <svg class="contact__icon" viewBox="0 0 24 24" aria-hidden="true"><path d="M6.6 10.8a15.1 15.1 0 0 0 6.6 6.6l2.2-2.2a1 1 0 0 1 1-.25 11.4 11.4 0 0 0 3.6.57 1 1 0 0 1 1 1V20a1 1 0 0 1-1 1A17 17 0 0 1 3 4a1 1 0 0 1 1-1h3.5a1 1 0 0 1 1 1c0 1.25.2 2.45.57 3.57a1 1 0 0 1-.25 1z"/></svg>
          1-844-555-0142
        </li>
        <li class="contact__item">
          <svg class="contact__icon" viewBox="0 0 24 24" aria-hidden="true"><path d="M2 6h20v12H2z M2 6l10 7 10-7" /></svg>
          info@yourmail.com
        </li>
        <li class="contact__item">
          <svg class="contact__icon" viewBox="0 0 24 24" aria-hidden="true"><circle cx="12" cy="12" r="10"/></svg>
          www.yourwebsite.com
        </li>
      </ul>
      <div class="contact__address">48 Maple Hollow Road<br>Fairview NY 11720</div>
    </div>
  </section>

  <section class="card card--back" aria-label="Rückseite">
    <div class="brand">
      <span class="brand__dot"></span>
      <div class="brand__name">SEELENLICHT</div>
      <div class="brand__person">MIRA LENZ</div>
    </div>
  </section>
</main>
</body>
</html>
```